Corvath Properties Business Card Design

We would now like to design business cards with the new Corvath Properties logo

Target Market(s)

Professional

Industry/Entity Type

Professional services

Contact Information for Business Card

Employee name, title, phone number, email address, corporate office address and logo.

Font styles to use
Sans Serif

Colors
0054AA
0677BA
7BADD7
CADEEF
E8F1F8

Requirements
Must have
• My logo
Should not have
• any other pictures or images besides my logo

```html
<!DOCTYPE html>
<html lang="en">
<head>
<meta charset="utf-8">
<title>Corvath Properties Business Card</title>
<link rel="stylesheet" href="https://fonts.googleapis.com/css2?family=Open+Sans:wght@400;600;700;800&display=swap">
<style>
  :root {
    --navy: #0054AA;
    --blue: #0677BA;
    --bright: #2F8FE6;
    --sky: #7BADD7;
    --mist: #CADEEF;
    --ice: #E8F1F8;
    --ink: #5a5f66;
    --paper: #ffffff;
    --backdrop: #ececec;
  }
  * { box-sizing: border-box; margin: 0; padding: 0; }
  html, body {
    width: 1200px; height: 943px; overflow: hidden;
    background: var(--backdrop);
    font-family: "Open Sans", sans-serif;
  }
  .canvas { position: relative; width: 1200px; height: 943px; }
  .card {
    position: absolute; width: 520px; height: 297px;
    border-radius: 3px; overflow: hidden;
    box-shadow: 0 10px 24px rgba(0,0,0,0.12);
  }

  /* Front: contact side */
  .card--front { left: 620px; top: 220px; background: var(--paper); }
  .person { position: absolute; left: 34px; top: 32px; }
  .person__name { font-size: 25px; font-weight: 800; color: var(--bright); letter-spacing: 1px; line-height: 1; }
  .person__title { font-size: 13px; color: var(--ink); margin-top: 4px; }
  .contact { position: absolute; left: 34px; top: 104px; width: 290px; list-style: none; }
  .contact li { display: flex; align-items: center; gap: 8px; font-size: 11.5px; color: var(--ink); line-height: 19px; white-space: nowrap; }
  .contact svg { width: 10px; height: 10px; fill: var(--blue); flex: none; }
  .brand-mark {
    position: absolute;
    display: flex; align-items: center; gap: 12px;
  }
  .card--front .brand-mark { right: 30px; top: 118px; }
  .brand-mark__square { width: 22px; height: 22px; background: var(--bright); flex: none; }
  .brand-mark__name { font-size: 22px; font-weight: 700; color: var(--bright); letter-spacing: 0.5px; line-height: 1.1; }
  .services {
    position: absolute; left: 0; right: 0; bottom: 18px; height: 28px;
    background: var(--bright); color: var(--paper);
    font-size: 11.5px; display: flex; align-items: center; justify-content: center; gap: 10px;
  }

  /* Back: brand side */
  .card--back {
    left: 60px; top: 430px;
    background: linear-gradient(115deg, #5f8ccd 0%, var(--sky) 45%, #8db4de 58%, #6690cb 100%);
    color: var(--paper);
  }
  .card--back .brand-mark { left: 40px; top: 44px; }
  .card--back .brand-mark__square { background: var(--paper); }
  .card--back .brand-mark__name { color: var(--paper); font-size: 26px; }
  .pledge { position: absolute; left: 150px; top: 128px; }
  .pledge__lead { font-size: 13px; font-weight: 600; margin-bottom: 6px; }
  .pledge__list { list-style: none; }
  .pledge__list li { font-size: 12.5px; line-height: 19px; padding-left: 14px; position: relative; }
  .pledge__list li::before { content: "•"; position: absolute; left: 0; }
</style>
</head>
<body>
<main class="canvas">

  <section class="card card--back" aria-label="Business card back">
    <div class="brand-mark">
      <span class="brand-mark__square"></span>
      <span class="brand-mark__name">Corvath Properties</span>
    </div>
    <div class="pledge">
      <p class="pledge__lead">Committed to Exceptional Service Since 1996</p>
      <ul class="pledge__list">
        <li>We bring people.</li>
        <li>We bring process.</li>
        <li>We bring “actionable” data.</li>
        <li>We bring robust technology.</li>
        <li>We bring a service provider ecosystem.</li>
      </ul>
    </div>
  </section>

  <section class="card card--front" aria-label="Business card front">
    <div class="person">
      <h1 class="person__name">JOHN DOE</h1>
      <p class="person__title">Corporate Offices</p>
    </div>
    <ul class="contact">
      <li><svg viewBox="0 0 10 10"><path d="M2 0.5l2 2-1 1.2c.6 1.3 1.6 2.3 2.9 2.9L7 5.6l2.2 2-1 1.8C4.5 9.2.8 5.5.6 1.6z"/></svg>555-014-2870</li>
      <li><svg viewBox="0 0 10 10"><path d="M0 2h10v6H0z M0 2l5 3.5L10 2" /></svg>info@corvathproperties.com</li>
      <li><svg viewBox="0 0 10 10"><circle cx="5" cy="5" r="4.5"/></svg>www.corvathproperties.com</li>
      <li><svg viewBox="0 0 10 10"><path d="M5 0a3.5 3.5 0 0 1 3.5 3.5C8.5 6 5 10 5 10S1.5 6 1.5 3.5A3.5 3.5 0 0 1 5 0z"/></svg>418 Harbor Road Suite 2, Lakeview, NJ 07999</li>
    </ul>
    <div class="brand-mark">
      <span class="brand-mark__square"></span>
      <span class="brand-mark__name">Corvath<br>Properties</span>
    </div>
    <div class="services">
      <span>Exterior Maintenance</span><span>•</span>
      <span>Interior Maintenance</span><span>•</span>
      <span>Construction &amp; Demolition</span>
    </div>
  </section>

</main>
</body>
</html>
```